Website design for an Italian restaurant in Amsterdam

I need a design for a client of mine. It is for Teatro Lunaverde, an Italian restaurant in Amsterdam.
We are going for a clean, modern look but we also need to realise an authentic feel.
The restaurant is located in an old movie theatre, that is where the name Teatro Lunaverde comes from.
Industry/Entity Type
Italian Restaurant
Number of Pages Required
1 page
Font styles to use
Sans Serif
Colors
Designer to choose colors to be used in the design.

```html
<!DOCTYPE html>
<html lang="nl">
<head>
<meta charset="utf-8">
<title>Teatro Lunaverde – Ristorante Italiano</title>
<link href="https://fonts.googleapis.com/css2?family=Roboto:wght@300;400;500;700&display=swap" rel="stylesheet">
<style>
:root{
  --orange:#f5a623;
  --orange-dark:#e8901a;
  --ink:#2b2b2b;
  --muted:#6d6d6d;
  --field:#ececec;
  --white:#ffffff;
  --hero-a:#5a3a22;
  --hero-b:#c2562a;
  --group-a:#7a2f10;
  --group-b:#f08a1e;
  --footer-a:#6b4a2a;
  --footer-b:#a8743c;
}
*{box-sizing:border-box;margin:0;padding:0}
html,body{width:1200px;height:2700px;overflow:hidden}
body{font-family:"Roboto",Arial,sans-serif;color:var(--ink);background:var(--white);position:relative}
.abs{position:absolute}

/* header */
.site-header{position:absolute;left:0;top:0;width:1200px;height:84px;background:var(--white);box-shadow:0 2px 6px rgba(0,0,0,.08);z-index:2}
.brand{position:absolute;left:20px;top:20px;display:flex;align-items:center;gap:12px}
.brand-dot{width:40px;height:40px;border-radius:50%;background:var(--orange)}
.brand-name{font-size:26px;font-weight:500;color:var(--ink);line-height:1}
.brand-tag{position:absolute;left:52px;top:32px;font-size:15px;color:var(--orange)}
.main-nav{position:absolute;left:418px;top:0;height:84px;display:flex}
.main-nav a{display:flex;align-items:center;height:84px;padding:0 26px;font-size:19px;font-weight:500;color:var(--ink);text-decoration:none}
.main-nav a.active{background:var(--orange);color:var(--white);padding:0 36px}
.nav-toggle{position:absolute;left:1154px;top:30px;width:30px;height:24px}
.nav-toggle span{display:block;height:4px;background:var(--orange);margin-bottom:6px;border-radius:2px}

/* hero */
.hero{position:absolute;left:0;top:84px;width:1200px;height:368px;background:radial-gradient(ellipse at 55% 55%,#e0742c 0%,var(--hero-b) 35%,var(--hero-a) 90%)}
.hero-phone{position:absolute;left:0;width:1200px;top:100px;text-align:center;font-size:40px;font-weight:300;color:var(--white);display:flex;justify-content:center;align-items:center;gap:14px}
.hero-btn{position:absolute;top:198px;height:46px;border:2px solid var(--white);color:var(--white);font-size:26px;font-weight:300;display:flex;align-items:center;justify-content:center}
.dots{position:absolute;top:338px;left:552px;display:flex;gap:12px}
.dots span{width:16px;height:16px;border-radius:50%;background:var(--white)}
.dots span.on{background:var(--orange);border:3px solid var(--white)}

/* section titles */
.section-title{position:absolute;left:0;width:1200px;text-align:center}
.flourish{display:block;margin:0 auto;width:150px;height:34px;border-radius:17px;background:linear-gradient(90deg,rgba(245,166,35,.15),rgba(245,166,35,.55),rgba(245,166,35,.15))}
.title-text{font-size:40px;font-weight:400;letter-spacing:16px;color:var(--ink);margin-top:8px;padding-left:16px}
.title-rule{width:410px;height:2px;background:var(--orange);margin:8px auto 0}
.on-dark .title-text{color:var(--white)}
.on-dark .title-rule{background:var(--white)}

/* menu */
.dish{position:absolute;width:308px;height:240px;border:3px solid var(--orange);background:linear-gradient(135deg,#f4f1ea,#b35a2f 55%,#6b4b2a)}
.dish.alt{background:linear-gradient(135deg,#f2efe8,#8a6a44 50%,#5e7a2e)}
.dish.ham{background:linear-gradient(135deg,#f5f2ec,#c86a5e 50%,#d9412a)}
.dish-price{position:absolute;left:0;top:0;width:100%;height:56px;background:rgba(140,100,30,.6);color:var(--white);font-size:26px;font-weight:300;text-align:center;line-height:56px}
.dish-name{position:absolute;left:0;bottom:0;width:100%;height:62px;background:rgba(140,100,30,.6);color:var(--white);font-size:26px;font-weight:300;line-height:62px;padding-left:6px;white-space:nowrap}
.slider-line{position:absolute;top:1115px;height:2px;background:var(--orange)}
.slider-btn{position:absolute;top:1102px;width:28px;height:28px;border-radius:50%;background:var(--orange);color:var(--white);font-size:24px;line-height:26px;text-align:center;font-weight:700}

/* group menu */
.group{position:absolute;left:0;top:1164px;width:1200px;height:362px;background:radial-gradient(ellipse at 60% 70%,var(--group-b) 0%,#c75a14 45%,var(--group-a) 100%)}
.group-row{position:absolute;left:222px;width:756px;height:44px;background:var(--white);display:flex;align-items:center;padding:0 12px;font-size:26px;font-weight:300;color:var(--ink)}
.group-row .leader{flex:1;border-bottom:2px dotted var(--ink);margin:0 4px 6px;height:1px;align-self:flex-end;margin-bottom:12px}
.group-row .price{color:var(--ink)}
.group-row .price b{color:var(--orange);font-weight:300}
.plus{display:inline-block;width:22px;height:22px;border-radius:50%;background:var(--orange);color:var(--white);font-size:20px;line-height:21px;text-align:center;font-weight:700;margin-left:8px}

/* reservation */
.field{position:absolute;left:186px;width:826px;height:50px;background:var(--field);color:var(--muted);font-size:22px;padding:0 14px;display:flex;align-items:center;justify-content:space-between}
.field.area{height:190px;align-items:flex-start;padding-top:12px}
.submit{position:absolute;left:494px;top:2292px;width:214px;height:60px;background:var(--orange);color:var(--white);font-size:28px;font-weight:300;display:flex;align-items:center;justify-content:center}
.to-top{position:absolute;left:1106px;top:2366px;width:48px;height:48px;border-radius:50%;background:var(--orange)}

/* footer */
.site-footer{position:absolute;left:0;top:2426px;width:1200px;height:274px;background:linear-gradient(120deg,var(--footer-a),var(--footer-b) 50%,#8a5a2c)}
.footer-brand{position:absolute;left:120px;top:30px;display:flex;align-items:center;gap:12px}
.footer-brand .brand-dot{background:var(--white);width:34px;height:34px}
.footer-brand .brand-name{color:var(--white);font-size:26px}
.footer-tag{position:absolute;left:240px;top:64px;color:var(--white);font-size:15px}
.contact-line{position:absolute;left:120px;color:var(--white);font-size:17px;display:flex;align-items:center;gap:16px}
.social{position:absolute;top:2636px;width:34px;height:34px;border-radius:50%;background:var(--white)}
.today-title{position:absolute;left:710px;top:2454px;color:var(--white);font-size:28px;font-weight:300}
.today-item{position:absolute;left:760px;display:flex;gap:10px;align-items:center;color:var(--white);font-size:16px;line-height:1.2}
.thumb{width:50px;height:46px;background:linear-gradient(135deg,#efe9dc,#9a6a3a);flex:none}
</style>
</head>
<body>

<header class="site-header">
  <div class="brand"><span class="brand-dot"></span><span class="brand-name">Teatro Lunaverde</span></div>
  <span class="brand-tag" style="left:72px;top:52px">Ristorante Italiano</span>
  <nav class="main-nav">
    <a class="active">HOME</a><a>MENU</a><a>GROEPSMENU</a><a>RESERVEREN</a><a>CONTACT</a>
  </nav>
  <div class="nav-toggle"><span></span><span></span><span></span></div>
</header>

<section class="hero" role="img" aria-label="Photo of a wood-fired pizza with basil, olives and tomatoes">
  <div class="hero-phone">
    <svg width="44" height="44" viewBox="0 0 24 24"><path fill="#fff" d="M6.6 10.8c1.4 2.8 3.8 5.1 6.6 6.6l2.2-2.2c.3-.3.7-.4 1-.2 1.1.4 2.3.6 3.6.6.6 0 1 .4 1 1V20c0 .6-.4 1-1 1C10.6 21 3 13.4 3 4c0-.6.4-1 1-1h3.5c.6 0 1 .4 1 1 0 1.3.2 2.5.6 3.6.1.3 0 .7-.2 1L6.6 10.8z"/></svg>
    <span>(+31) 20 555 0192</span>
  </div>
  <div class="hero-btn" style="left:422px;width:114px">Reserveren</div>
  <div class="hero-btn" style="left:618px;width:168px">Contact</div>
  <div class="dots"><span class="on"></span><span></span><span></span><span></span></div>
</section>

<div class="section-title" style="top:470px">
  <span class="flourish" role="img" aria-label="Ornamental flourish"></span>
  <div class="title-text">MENU</div>
  <div class="title-rule"></div>
</div>

<div class="dish" style="left:124px;top:590px" role="img" aria-label="Photo of a grilled lobster dish">
  <div class="dish-price">€ 4,50</div>
  <div class="dish-name">Pane Burro e Tapanada</div>
</div>
<div class="dish alt" style="left:446px;top:590px" role="img" aria-label="Photo of risotto with green asparagus"></div>
<div class="dish ham" style="left:766px;top:590px" role="img" aria-label="Photo of prosciutto with bruschetta"></div>
<div class="dish alt" style="left:124px;top:842px" role="img" aria-label="Photo of risotto with green asparagus"></div>
<div class="dish ham" style="left:446px;top:842px" role="img" aria-label="Photo of prosciutto with bruschetta"></div>
<div class="dish" style="left:766px;top:842px" role="img" aria-label="Photo of a grilled lobster dish"></div>

<div class="slider-line" style="left:130px;width:370px"></div>
<div class="slider-btn" style="left:536px">−</div>
<div class="slider-btn" style="left:636px">+</div>
<div class="slider-line" style="left:700px;width:370px"></div>

<section class="group" role="img" aria-label="Photo of spaghetti with tomato sauce, parmesan and basil">
  <div class="section-title on-dark" style="top:22px">
    <span class="flourish" role="img" aria-label="Ornamental flourish"></span>
    <div class="title-text">GROEPSMENU</div>
    <div class="title-rule"></div>
  </div>
  <div class="group-row" style="top:154px">Groepsmenu Speciale<span class="leader"></span><span class="price">(<b>€ 34,50</b>)</span><span class="plus">+</span></div>
  <div class="group-row" style="top:242px">Groepsmenu Royal<span class="leader"></span><span class="price">(<b>€ 49,50</b>)</span><span class="plus">+</span></div>
  <div class="abs" style="left:300px;top:328px;width:600px;height:2px;background:var(--white)"></div>
</section>

<div class="section-title" style="top:1540px">
  <span class="flourish" role="img" aria-label="Ornamental flourish"></span>
  <div class="title-text">RESERVEREN</div>
  <div class="title-rule"></div>
</div>

<div class="field" style="top:1656px">Naam :</div>
<div class="field" style="top:1726px">Email :</div>
<div class="field" style="top:1796px">Tel :</div>
<div class="field" style="top:1866px">Aantal Gasten :<span class="plus">+</span></div>
<div class="field" style="top:1936px">Datum :<span class="plus">+</span></div>
<div class="field" style="top:2006px">Tijd :<span class="plus">+</span></div>
<div class="field area" style="top:2076px">Opmerking :</div>
<div class="submit">Reserveren</div>
<div class="abs" style="left:240px;top:2389px;width:730px;height:2px;background:var(--orange)"></div>
<div class="to-top">
  <svg width="48" height="48" viewBox="0 0 48 48"><path d="M17 28l7-7 7 7" fill="none" stroke="#fff" stroke-width="3" stroke-linecap="round" stroke-linejoin="round"/></svg>
</div>

<footer class="site-footer" role="img" aria-label="Photo of tomatoes, onions, pasta and olive oil on a wooden table">
  <div class="footer-brand"><span class="brand-dot"></span><span class="brand-name">Teatro Lunaverde</span></div>
  <span class="footer-tag">Ristorante Italiano</span>
  <div class="contact-line" style="top:104px">
    <svg width="18" height="24" viewBox="0 0 18 24"><path fill="#fff" d="M9 0C4 0 0 4 0 9c0 6.5 9 15 9 15s9-8.5 9-15c0-5-4-9-9-9zm0 12.5A3.5 3.5 0 1 1 9 5.5a3.5 3.5 0 0 1 0 7z"/></svg>
    <span>Lunastraat 18, 1015 AB Amsterdam</span>
  </div>
  <div class="contact-line" style="top:154px">
    <svg width="20" height="20" viewBox="0 0 24 24"><path fill="#fff" d="M6.6 10.8c1.4 2.8 3.8 5.1 6.6 6.6l2.2-2.2c.3-.3.7-.4 1-.2 1.1.4 2.3.6 3.6.6.6 0 1 .4 1 1V20c0 .6-.4 1-1 1C10.6 21 3 13.4 3 4c0-.6.4-1 1-1h3.5c.6 0 1 .4 1 1 0 1.3.2 2.5.6 3.6.1.3 0 .7-.2 1L6.6 10.8z"/></svg>
    <span>(+31) 20 555 0192</span>
  </div>
  <div class="today-title" style="top:28px">Vandaag op de kaart</div>
  <div class="today-item" style="top:96px"><span class="thumb" role="img" aria-label="Photo of sea bream with pistachio"></span><span>Orata al Pistacchio</span></div>
  <div class="today-item" style="top:156px"><span class="thumb" role="img" aria-label="Photo of beef fillet with gorgonzola"></span><span>Filetto di Manzo al<br>Gorgonzola e Noci</span></div>
  <div class="today-item" style="top:214px"><span class="thumb" role="img" aria-label="Photo of aubergine parmigiana"></span><span>Melanzana alla<br>Parmigiana</span></div>
</footer>
<div class="social" style="left:120px"></div>
<div class="social" style="left:172px"></div>

</body>
</html>
```